Need business cards for our e-assessment business

We need professional looking business cards for our e-assessment business based in Europe. Our company is called Velmora.

You can just use sample name and addresses.

The colours we use are:

#70abe4 (blue)
#FF6600 (orange)

The back side should say: Online testing made simple

This is the print-shop we are using. Please look at the link for info about formats: http://nl.pribbly-print.com/help/faq/using-my-own-artwork.html

Target Market(s)

Target market is education and large corporations

Industry/Entity Type

Business

```html
<!DOCTYPE html>
<html lang="en">
<head>
<meta charset="utf-8">
<title>Velmora business cards</title>
<link rel="stylesheet" href="https://fonts.googleapis.com/css2?family=Barlow:wght@400;500&display=swap">
<style>
  :root {
    --backdrop: #e6e7e9;
    --card-white: #f7f7f7;
    --brand-orange: #e05a00;
    --brand-blue: #70abe4;
    --ink: #3a3a3a;
    --on-orange: #fbe9dc;
    --mark-light: #f1f1f1;
  }
  * { margin: 0; padding: 0; box-sizing: border-box; }
  html, body {
    width: 1200px; height: 800px; overflow: hidden;
    background: var(--backdrop);
    font-family: "Barlow", Arial, sans-serif;
  }
  .canvas { position: relative; width: 1200px; height: 800px; }
  .card {
    position: absolute; left: 361px;
    width: 478px; height: 306px;
  }
  .card--front { top: 72px; background: var(--card-white); }
  .card--back { top: 418px; background: var(--brand-orange); color: var(--on-orange); }

  .brand-dot {
    position: absolute; left: 96px; top: 107px;
    width: 92px; height: 92px; border-radius: 50%;
    background: var(--brand-orange);
  }
  .brand-name {
    position: absolute; left: 210px; top: 122px;
    font-size: 54px; font-weight: 500; line-height: 1;
    color: var(--ink); letter-spacing: -0.5px;
  }
  .tagline {
    position: absolute; left: 0; right: 0; top: 254px;
    text-align: center;
  }
  .tagline__rule {
    display: block; width: 180px; height: 1px; margin: 0 auto 6px;
    background: var(--brand-blue);
  }
  .tagline__text {
    font-size: 15px; color: var(--brand-blue); letter-spacing: 0.3px;
  }

  .back-mark {
    position: absolute; left: 59px; top: 26px;
    width: 78px; height: 78px; border-radius: 50%;
    background: var(--mark-light);
  }
  .contact {
    position: absolute; left: 57px; top: 142px;
    font-size: 13px; letter-spacing: 0.4px; line-height: 17px;
  }
  .contact__name { font-size: 21px; line-height: 24px; margin-bottom: 6px; }
  .contact__role { font-size: 14px; letter-spacing: 1px; margin-left: 10px; }
  .contact__block { margin-bottom: 8px; }
  .contact__web { margin-top: 16px; }
</style>
</head>
<body>
<main class="canvas">
  <section class="card card--front" aria-label="Card front">
    <span class="brand-dot"></span>
    <span class="brand-name">velmora</span>
    <p class="tagline">
      <span class="tagline__rule"></span>
      <span class="tagline__text">Online testing made simple</span>
    </p>
  </section>

  <section class="card card--back" aria-label="Card back">
    <span class="back-mark"></span>
    <div class="contact">
      <p class="contact__name">Jonas Verbeek<span class="contact__role">MANAGER</span></p>
      <div class="contact__block">
        <p>MOBILE&nbsp; 0150 7291846&nbsp; |&nbsp; PHONE&nbsp; 0655 284 7719</p>
        <p>EMAIL&nbsp; verbeek@velmora.nl</p>
      </div>
      <div class="contact__block">
        <p>Lindenhoflaan 41, 2514 KD&nbsp; ‘S-Gravenhage</p>
        <p>NETHERLANDS</p>
      </div>
      <p class="contact__web">www.velmora.nl</p>
    </div>
  </section>
</main>
</body>
</html>
```